Redesign Login page

I want to redesign my login page to bring my 2 products closer together. I am only looking to redesign one login page, not 2.

For the logo, please make it solid and it can be black or white if helpful. I can also fine tune the logo if you get it close.

Coding

Coded - Design and coding required

Number of Pages Required

1 page

```html
<!DOCTYPE html>
<html lang="en">
<head>
<meta charset="utf-8">
<title>Northvale – Log in</title>
<link href="https://fonts.googleapis.com/css2?family=Roboto:wght@400;500;700&display=swap" rel="stylesheet">
<style>
  :root {
    --page-bg: #ffffff;
    --card-bg: #ffffff;
    --card-shadow: rgba(40, 75, 70, 0.28);
    --ink: #1c1c1c;
    --brand-dark: #03302c;
    --brand-mark: #8f1f1a;
    --link-muted: #4b6c67;
    --field-border: #d3d6dc;
    --placeholder: #8a94a3;
    --button-text: #ffffff;
  }
  * { box-sizing: border-box; margin: 0; padding: 0; }
  html, body {
    width: 1200px;
    height: 808px;
    overflow: hidden;
    background: var(--page-bg);
    font-family: "Roboto", Arial, sans-serif;
    color: var(--ink);
  }
  .login-card {
    position: absolute;
    left: 327px;
    top: 93px;
    width: 547px;
    height: 622px;
    background: var(--card-bg);
    border-radius: 6px;
    box-shadow: 0 0 12px 2px var(--card-shadow);
  }
  .brand {
    position: absolute;
    left: 0;
    right: 0;
    top: 92px;
    text-align: center;
    font-size: 50px;
    font-weight: 700;
    letter-spacing: 0.5px;
    color: var(--brand-mark);
    line-height: 1;
  }
  .login-form {
    position: absolute;
    left: 66px;
    top: 230px;
    width: 415px;
  }
  .field-label {
    display: block;
    font-size: 12.5px;
    line-height: 15px;
    margin-bottom: 4px;
  }
  .field {
    position: relative;
    width: 415px;
    height: 34px;
    border: 1px solid var(--field-border);
    border-radius: 6px;
    display: flex;
    align-items: center;
    padding: 0 11px;
  }
  .field input {
    border: 0;
    outline: 0;
    width: 100%;
    background: transparent;
    font: 400 10px "Roboto", Arial, sans-serif;
    color: var(--ink);
  }
  .field input::placeholder { color: var(--placeholder); }
  .field .reveal {
    position: absolute;
    right: 16px;
    top: 11px;
  }
  .switch-user {
    display: block;
    margin-top: 7px;
    font-size: 12.5px;
    color: var(--brand-dark);
    text-decoration: none;
  }
  .password-group { margin-top: 30px; }
  .form-row {
    display: flex;
    justify-content: space-between;
    align-items: center;
    margin-top: 30px;
  }
  .save-id {
    display: flex;
    align-items: center;
    gap: 4px;
    font-size: 12.5px;
  }
  .forgot-password {
    font-size: 12.5px;
    color: var(--brand-dark);
    text-decoration: none;
  }
  .login-button {
    display: block;
    width: 415px;
    height: 37px;
    margin-top: 30px;
    border: 0;
    border-radius: 6px;
    background: var(--brand-dark);
    color: var(--button-text);
    font: 500 15px "Roboto", Arial, sans-serif;
  }
  .support-links {
    display: flex;
    justify-content: center;
    gap: 34px;
    margin-top: 30px;
  }
  .support-links a {
    font-size: 17px;
    font-weight: 500;
    color: var(--link-muted);
    text-decoration: underline;
    text-underline-offset: 2px;
  }
</style>
</head>
<body>
  <main class="login-card">
    <div class="brand">Northvale</div>
    <form class="login-form">
      <label class="field-label" for="user-id">User ID</label>
      <div class="field">
        <input id="user-id" type="email" placeholder="Example@email.com">
      </div>
      <a class="switch-user" href="#">log in with another user ID</a>

      <div class="password-group">
        <label class="field-label" for="password">Password</label>
        <div class="field">
          <input id="password" type="password" placeholder="At least 8 characters">
          <svg class="reveal" width="14" height="10" viewBox="0 0 14 10" aria-hidden="true">
            <path d="M1 5 C3 1.5 11 1.5 13 5 C11 8.5 3 8.5 1 5 Z" fill="none" stroke="#7d8796" stroke-width="1.2"/>
            <circle cx="7" cy="5" r="1.7" fill="#7d8796"/>
          </svg>
        </div>
      </div>

      <div class="form-row">
        <label class="save-id">
          <svg width="13" height="13" viewBox="0 0 13 13" aria-hidden="true">
            <circle cx="6.5" cy="6.5" r="6.5" fill="#3f5a56"/>
            <path d="M3.6 6.7 L5.6 8.6 L9.4 4.6" fill="none" stroke="#fff" stroke-width="1.3" stroke-linecap="round" stroke-linejoin="round"/>
          </svg>
          Save ID
        </label>
        <a class="forgot-password" href="#">Forgot Password?</a>
      </div>

      <button class="login-button" type="submit">log in</button>

      <nav class="support-links">
        <a href="#">Forget User ID</a>
        <a href="#">Help</a>
        <a href="#">Enroll In Online Acccess</a>
      </nav>
    </form>
  </main>
</body>
</html>
```